New Shop front sign with 2 x window sign designs

I require a New shop sign for a retail store. with 2 x window design for printing onto diabond material. it must be bright and fresh. please see images of sizes required.
Updates

Please see a similar logo for the top sign, it shows Vantro. but we require the same or similar (better) design saying Plum stall. It will be on a plain backgroung of white, with the slogan at the bottom most items below £1. and also a seperate area for the "small family owned business" I just want a plain simple top sign that is professional and stylish. please see the upload area wher i have added the vantro logo. i look forward to your designs coming through to me,

Target Market(s)

This is for a retail store, and it needs to reflect our cheap prices.

Industry/Entity Type

Retail

Requirements
Must have
• For the top sign, it must say "The Plum Stall" in bigger text as the main sign. and under the main words, we need to have a slogan similar to "Big Brands Better Prices - Most products under £1"
• Also on the top sign, I would like to add "local family run business"
• The backround needs to reflect cheap prices, maybe like £ signs and good artwork.
• The first window sign, needs to be about our cheap mr quandle ice cream, where it will be sold for 89p. it must have a cornet cone with soft icecream top. with good artwork, advertising the low price of only 99p.
• The second window needs to advertise our slush, small slush 89p - Large £1.39 - Yard Cup £1.99
• Please see attached similar artwork on my previous tasks.
Nice to have
• It is nice to have a full bright design that will invite customers to my store whilst walking past
Should not have
• I do not require a basic design, this must be top of the range professional crisp and clean.

```html
<!DOCTYPE html>
<html lang="en">
<head>
<meta charset="utf-8">
<title>The Plum Stall – Shop Sign</title>
<link rel="stylesheet" href="https://fonts.googleapis.com/css2?family=Arimo:wght@700&family=Open+Sans:wght@400;600&display=swap">
<style>
  :root {
    --page: #ffffff;
    --orange-deep: #f4572a;
    --orange: #f8932a;
    --orange-soft: #fbb03b;
    --sun: #fff36e;
    --palm: #f7a12e;
    --palm-light: #fbc04a;
    --red: #f03c14;
    --red-text: #ee3a12;
    --white: #ffffff;
    --teal: #23c4d0;
    --teal-dark: #1aa9c2;
    --text-shadow: rgba(200, 70, 10, 0.75);
  }
  html, body {
    margin: 0;
    padding: 0;
    width: 1200px;
    height: 334px;
    overflow: hidden;
    background: var(--page);
  }
  .shop-sign {
    position: absolute;
    left: 64px;
    top: 42px;
    width: 1072px;
    height: 233px;
    overflow: hidden;
    background:
      radial-gradient(circle at 93% 18%, var(--sun) 0, rgba(255, 243, 110, 0.85) 12%, rgba(251, 176, 59, 0) 45%),
      linear-gradient(90deg, var(--orange-deep) 0%, var(--orange) 22%, var(--orange-soft) 60%, #fcd04c 100%);
    box-shadow: 0 4px 14px rgba(0, 0, 0, 0.4);
  }
  .palms {
    position: absolute;
  }
  .palms--left {
    left: 0;
    top: 0;
    width: 190px;
    height: 233px;
    background: radial-gradient(ellipse at 30% 30%, var(--palm-light) 0, rgba(247, 161, 46, 0.6) 45%, rgba(247, 161, 46, 0) 75%);
  }
  .palms--right {
    right: 0;
    top: 40px;
    width: 260px;
    height: 193px;
    background: radial-gradient(ellipse at 60% 70%, rgba(247, 145, 40, 0.85) 0, rgba(247, 161, 46, 0.4) 50%, rgba(247, 161, 46, 0) 78%);
  }
  .shop-name {
    position: absolute;
    left: 196px;
    top: 14px;
    margin: 0;
    font-family: "Open Sans", sans-serif;
    font-weight: 400;
    color: var(--white);
    text-shadow: 3px 3px 0 var(--text-shadow);
    line-height: 1;
  }
  .shop-name__the {
    display: block;
    font-weight: 600;
    font-size: 28px;
    letter-spacing: 1px;
  }
  .shop-name__word {
    display: block;
    font-size: 86px;
    letter-spacing: -1px;
    line-height: 0.92;
  }
  .shop-name__word--second {
    margin-left: 18px;
  }
  .family-badge {
    position: absolute;
    left: 0;
    top: 150px;
    width: 179px;
    height: 56px;
    box-sizing: border-box;
    padding: 6px 0 0 12px;
    background: linear-gradient(90deg, var(--teal-dark), var(--teal));
    box-shadow: 2px 3px 6px rgba(0, 0, 0, 0.3);
    font-family: "Open Sans", sans-serif;
    font-size: 18px;
    line-height: 21px;
    color: var(--white);
  }
  .slogan {
    position: absolute;
    left: 520px;
    top: 46px;
    font-family: "Arimo", sans-serif;
    font-weight: 700;
    line-height: 1;
  }
  .slogan__line {
    display: block;
    white-space: nowrap;
  }
  .slogan__brands {
    font-size: 40px;
    color: var(--red-text);
    -webkit-text-stroke: 1px rgba(255, 255, 255, 0.7);
    text-shadow: 2px 2px 0 rgba(200, 70, 10, 0.4);
  }
  .slogan__prices {
    margin-top: 18px;
    font-size: 40px;
    color: var(--white);
    text-shadow: 2px 2px 0 var(--text-shadow);
  }
  .slogan__under {
    margin-top: 17px;
    font-size: 25px;
    color: var(--red-text);
  }
  .price-badge {
    position: absolute;
    left: 868px;
    top: 85px;
    width: 128px;
    height: 128px;
  }
</style>
</head>
<body>
  <section class="shop-sign">
    <div class="palms palms--left" role="img" aria-label="Palm tree silhouettes"></div>
    <div class="palms palms--right" role="img" aria-label="Palm tree silhouettes"></div>

    <h1 class="shop-name">
      <span class="shop-name__the">THE</span>
      <span class="shop-name__word">PLUM</span>
      <span class="shop-name__word shop-name__word--second">STALL</span>
    </h1>

    <div class="family-badge">LOCAL FAMILY<br>RUN BUSINESS</div>

    <p class="slogan">
      <span class="slogan__line slogan__brands">BIG BRANDS</span>
      <span class="slogan__line slogan__prices">BETTER PRICES</span>
      <span class="slogan__line slogan__under">MOST PRODUCTS UNDER</span>
    </p>

    <svg class="price-badge" viewBox="0 0 128 128" aria-label="£1">
      <circle cx="64" cy="64" r="64" fill="var(--red)"/>
      <text x="62" y="88" text-anchor="middle" font-family="Arimo, sans-serif" font-weight="700" font-size="70" fill="var(--white)">£1</text>
    </svg>
  </section>
</body>
</html>
```